New Plumbing Company

We are looking for a smart and creative business card design for our new plumbing company. We are looking for creativity and originality in our business cards.

Industry/Entity Type

Plumbing

Contact Information for Business Card

Crestline Plumbing
Peter Halvane
Managing Director
Telephone Number : 0481529604
Email : service@crestlineplumbing.com.au
Website : www.crestlineplumbing.com.au
Lic. 508264K

Colors
0692cd
33a6d7
000000

Requirements
Must have
• I want the business card to be designed on a black background using the blue tones i have selected as seen in the company logo.

```html
<!DOCTYPE html>
<html lang="en">
<head>
<meta charset="utf-8">
<title>Crestline Plumbing – Business Card</title>
<link href="https://fonts.googleapis.com/css2?family=Lato:wght@400;700;900&display=swap" rel="stylesheet">
<style>
  :root {
    --page-bg: #d9d9d9;
    --card-black: #231f20;
    --card-white: #ffffff;
    --brand-blue: #0692cd;
    --brand-blue-deep: #1565b0;
    --brand-blue-fold: #0d4a80;
    --stripe-blue: #c9e0f2;
    --ink: #1a1a1a;
    --logo-white: #ffffff;
  }
  * { box-sizing: border-box; margin: 0; padding: 0; }
  html, body {
    width: 1200px; height: 800px; overflow: hidden;
    background: var(--page-bg);
    font-family: 'Lato', sans-serif;
  }
  .card {
    position: absolute; left: 180px; top: 160px;
    width: 840px; height: 480px;
    display: flex;
    box-shadow: 0 8px 24px rgba(0,0,0,0.18);
  }
  .card-brand {
    width: 460px; height: 100%;
    background: var(--card-black);
    display: flex; align-items: center; justify-content: center; gap: 16px;
  }
  .brand-dot {
    width: 22px; height: 22px; border-radius: 50%;
    background: var(--brand-blue);
  }
  .brand-name {
    color: var(--logo-white);
    font-weight: 400; font-size: 36px; letter-spacing: 0.5px;
  }
  .card-stripe {
    width: 46px; height: 100%;
    background: var(--stripe-blue);
  }
  .card-details {
    flex: 1; height: 100%;
    background: var(--card-white);
    padding: 72px 0 0 36px;
    color: var(--ink);
  }
  .holder-name { font-weight: 900; font-size: 38px; line-height: 1; }
  .holder-role { font-size: 17px; letter-spacing: 1px; margin-top: 8px; }
  .contact-list { list-style: none; margin-top: 44px; }
  .contact-list li { height: 40px; line-height: 40px; font-size: 18px; letter-spacing: 0.5px; }
  .contact-list li.small { font-size: 15px; }
  .tabs { position: absolute; left: 448px; top: 0; }
  .tab { position: absolute; left: 0; width: 70px; height: 36px; }
</style>
</head>
<body>
  <section class="card">
    <div class="card-brand">
      <span class="brand-dot"></span>
      <span class="brand-name">Crestline Plumbing</span>
    </div>
    <div class="card-stripe"></div>
    <div class="card-details">
      <h1 class="holder-name">Peter Halvane</h1>
      <p class="holder-role">Managing Director</p>
      <ul class="contact-list">
        <li>0481529604</li>
        <li>0481529604</li>
        <li class="small">service@crestlineplumbing.com.au</li>
        <li class="small">www.crestlineplumbing.com.au</li>
        <li>your street adress</li>
        <li class="small">Lic. 508264K</li>
      </ul>
    </div>

    <div class="tabs" aria-hidden="true">
      <svg class="tab" style="top:76px;height:48px" viewBox="0 0 70 48">
        <polygon points="0,0 8,0 8,6" fill="var(--brand-blue-fold)"/>
        <rect x="0" y="0" width="62" height="48" rx="4" fill="var(--brand-blue-deep)"/>
        <circle cx="31" cy="18" r="6" fill="#fff"/>
        <path d="M19 34 q12 -14 24 0 z" fill="#fff"/>
      </svg>
      <svg class="tab" style="top:186px" viewBox="0 0 70 36">
        <rect x="0" y="0" width="62" height="36" rx="4" fill="var(--brand-blue-deep)"/>
        <path d="M20 14 q11 -8 22 0 l-3 4 h-4 v-3 h-8 v3 h-4 z" fill="#fff"/>
        <rect x="23" y="19" width="16" height="9" rx="1" fill="#fff"/>
      </svg>
      <svg class="tab" style="top:226px" viewBox="0 0 70 36">
        <rect x="0" y="0" width="62" height="36" rx="4" fill="var(--brand-blue-deep)"/>
        <rect x="24" y="8" width="14" height="6" fill="#fff"/>
        <rect x="19" y="15" width="24" height="10" rx="2" fill="#fff"/>
        <rect x="24" y="23" width="14" height="6" fill="#fff"/>
      </svg>
      <svg class="tab" style="top:266px" viewBox="0 0 70 36">
        <rect x="0" y="0" width="62" height="36" rx="4" fill="var(--brand-blue-deep)"/>
        <rect x="19" y="9" width="24" height="17" fill="none" stroke="#fff" stroke-width="2"/>
        <path d="M19 9 l12 10 l12 -10" fill="none" stroke="#fff" stroke-width="2"/>
      </svg>
      <svg class="tab" style="top:306px" viewBox="0 0 70 36">
        <rect x="0" y="0" width="62" height="36" rx="4" fill="var(--brand-blue-deep)"/>
        <rect x="20" y="8" width="22" height="15" fill="none" stroke="#fff" stroke-width="2"/>
        <rect x="27" y="25" width="8" height="3" fill="#fff"/>
      </svg>
      <svg class="tab" style="top:346px" viewBox="0 0 70 36">
        <rect x="0" y="0" width="62" height="36" rx="4" fill="var(--brand-blue-deep)"/>
        <path d="M18 19 l13 -11 l13 11" fill="none" stroke="#fff" stroke-width="3"/>
        <path d="M22 18 v10 h6 v-6 h6 v6 h6 v-10 l-9 -7 z" fill="#fff"/>
      </svg>
    </div>
  </section>
</body>
</html>
```